Capability Statement Document/Flyer

Take the existing words from the capability statement document (attached) and design a unique folder/flyer document for professional use. Maybe something like a trifold or bifold style. Use approved colours and logo as per the attached files.
Our company designs and builds small onshore gas processing plants.

```html
<!DOCTYPE html>
<html lang="en">
<head>
<meta charset="utf-8">
<title>Veridan PDP Capability Trifold</title>
<link href="https://fonts.googleapis.com/css2?family=Inter:wght@400;500;600;700&display=swap" rel="stylesheet">
<style>
:root{
  --teal:#0b7a68;
  --teal-text:#0e7a6a;
  --teal-deep:#0f5a4f;
  --teal-avatar:#236f63;
  --mint:#98d3c8;
  --panel:#e1e9ea;
  --cell-grey:#dcdcdc;
  --rule:#8f9696;
  --ink:#151515;
  --band-side:#4a4a4a;
  --band-mid:#222222;
}
*{box-sizing:border-box;margin:0;padding:0}
html,body{width:1200px;height:907px;overflow:hidden;background:#fff}
body{font-family:"Inter",Arial,sans-serif;color:var(--ink)}
.stage{position:absolute;left:0;top:0;width:2212px;height:1672px;transform:scale(0.5425);transform-origin:0 0}
.abs{position:absolute}
.panel{position:absolute;top:238px;width:634px;height:1275px;background:var(--panel);overflow:hidden}
.panel--services{left:223px}
.panel--roles{left:857px}
.panel--people{left:1491px}
.band{position:absolute;top:1513px;height:45px;width:634px}
.band--left{left:223px;background:var(--band-side)}
.band--mid{left:857px;background:var(--band-mid)}
.band--right{left:1491px;background:var(--band-side)}
.heading{color:var(--teal-text);font-weight:700;font-size:31px;line-height:1.2}

/* services table */
.services-table{position:absolute;left:17px;top:67px;width:600px;border-collapse:collapse;table-layout:fixed;font-size:15px;line-height:20px}
.services-table col.c-num{width:40px}
.services-table col.c-fn{width:213px}
.services-table col.c-svc{width:347px}
.services-table th{background:var(--teal);color:#fff;font-weight:600;text-align:left;height:43px;padding:0 8px}
.services-table td{border:1px solid var(--rule);padding:0 8px}
.services-table td.num{background:var(--teal);color:#fff;font-weight:600;text-align:center;border-color:var(--teal)}
.services-table td.fn{font-weight:600;padding-left:10px}
.services-table tr{height:53px}
.services-table tr.tall{height:69px}

.objective-text{position:absolute;left:19px;top:855px;width:590px;font-size:16px;line-height:29px}
.photo-zone{position:absolute;left:0;top:922px;width:634px;height:353px;
  background:linear-gradient(180deg,#e1e9ea 0%,#b9c3cc 35%,#a9b3bc 62%,#8e8f90 85%,#6b6a66 100%)}
.contact-left{position:absolute;left:97px;top:988px;display:flex;align-items:center;gap:16px}
.contact-left .icon{width:84px;height:84px}
.contact-left p{font-size:23px;line-height:37px;color:#111}
.contact-left strong{font-weight:700}

/* roles */
.roles-title{position:absolute;left:33px;top:34px;color:#fff;font-weight:700;font-size:63px;line-height:71px}
.roles-table{position:absolute;left:33px;top:294px;width:571px;border-collapse:collapse;table-layout:fixed;font-size:15px}
.roles-table col.c-owner{width:224px}
.roles-table col.c-svc{width:347px}
.roles-table th{background:var(--teal-deep);color:#fff;font-weight:600;text-align:left;height:43px;padding:0 19px}
.roles-table td{background:var(--cell-grey);border:1px solid var(--rule);height:53px;padding:0 6px 0 19px;white-space:nowrap}
.roles-table td.owner{font-weight:600;font-size:14.5px}
.roles-table td.svc{font-size:14.5px;color:#222}
.ticks{position:absolute;left:33px;list-style:none;font-size:15.5px}
.ticks li{height:31.6px;display:flex;align-items:center;gap:10px}
.ticks svg{width:14px;height:14px;flex:none}

/* people */
.people-title{position:absolute;left:29px;top:24px;color:var(--teal-text);font-weight:700;font-size:64px;line-height:71px}
.rule{position:absolute;left:27px;width:580px;height:1px;background:#b6cfcb}
.person{position:absolute;left:27px;width:590px}
.avatar{position:absolute;left:0;top:0;width:110px;height:110px}
.person-body{position:absolute;left:129px;top:0;width:460px;font-size:15px;line-height:20.5px}
.person-head{display:flex;justify-content:space-between;color:var(--teal-text);font-weight:600;margin-bottom:20px}
.person-body .firms{font-weight:700}
.contact-box{position:absolute;left:44px;top:1128px;width:547px;height:116px;background:var(--teal-avatar);border-radius:6px;color:#fff;font-size:31px;line-height:37px;padding:20px 0 0 59px}
.contact-box strong{font-weight:700}
</style>
</head>
<body>
<div class="stage">

  <section class="panel panel--services">
    <h2 class="heading abs" style="left:20px;top:14px">PDP Services:</h2>
    <table class="services-table">
      <colgroup><col class="c-num"><col class="c-fn"><col class="c-svc"></colgroup>
      <thead><tr><th style="text-align:center">#</th><th>Function</th><th>Veridan Service</th></tr></thead>
      <tbody>
        <tr style="height:54px"><td class="num">1</td><td class="fn">Project Management</td><td>Planning, Reporting &amp; Delivery Leadership from Concept to Completion</td></tr>
        <tr><td class="num">2</td><td class="fn">Engineering</td><td>Concept Selection, Design Coordination, Technical Assurance &amp; Value Engineering</td></tr>
        <tr><td class="num">3</td><td class="fn">Procurement</td><td>Contracting Strategy, Tender Process &amp; Supplier/Contractor Management</td></tr>
        <tr style="height:52px"><td class="num">4</td><td class="fn">Approvals</td><td>Land Access, Regulator Engagement, Safety Case, Permits &amp; Licenses</td></tr>
        <tr style="height:54px"><td class="num">5</td><td class="fn">Cost Control</td><td>Budget Development, Forecasting &amp; Management</td></tr>
        <tr style="height:52px"><td class="num">6</td><td class="fn">Scheduling</td><td>Master Schedule Development, WBS, Resource Allocation, Monitoring &amp; Updating</td></tr>
        <tr style="height:52px"><td class="num">7</td><td class="fn">Risk Management</td><td>Risk Register, Identification, Mitigation &amp; Reporting</td></tr>
        <tr><td class="num">8</td><td class="fn">Governance</td><td>Framework, Stage Gates, Change control, Reporting &amp; Decision Support</td></tr>
        <tr><td class="num">9</td><td class="fn">Construction</td><td>Management &amp; Coordination of Contractor Execution Teams</td></tr>
        <tr class="tall"><td class="num">10</td><td class="fn">Commissioning &amp;<br>Start-up</td><td>Lead Commissioning &amp; Start-up, Completions System, Bring the Facility to Steady-State</td></tr>
        <tr style="height:55px"><td class="num">11</td><td class="fn">Operations Readiness</td><td>People &amp; Organisation, Process &amp; Procedures, Systems &amp; Technology</td></tr>
        <tr style="height:54px"><td class="num">12</td><td class="fn">Operations &amp; Maintenance</td><td>Monitor &amp; Operate Asset, Minimize Downtime, Lowest Possible OPEX for Owner</td></tr>
      </tbody>
    </table>
    <h2 class="heading abs" style="left:17px;top:804px">PDP Objective:</h2>
    <p class="objective-text">Deliver the project safely, on schedule, within budget and ready for operations; providing owner capability throughout the project lifecycle.</p>
    <div class="photo-zone" role="img" aria-label="Photograph of a solar panel array beside a small onshore gas processing plant under a pale sky"></div>
    <div class="contact-left">
      <svg class="icon" viewBox="0 0 84 84" aria-hidden="true">
        <circle cx="42" cy="42" r="42" fill="#0e6b5e"/>
        <rect x="21" y="27" width="42" height="30" rx="5" fill="none" stroke="#fff" stroke-width="3"/>
        <path d="M23 31 L42 45 L61 31" fill="none" stroke="#fff" stroke-width="3" stroke-linejoin="round"/>
      </svg>
      <p><strong>For More Information Contact:</strong><br>directors@veridan.com.au</p>
    </div>
  </section>

  <section class="panel panel--roles">
    <svg class="abs" style="left:0;top:0" width="634" height="1275" aria-hidden="true">
      <polygon points="0,0 634,0 634,548 0,437" fill="var(--teal)"/>
      <polygon points="0,1127 243,1182 0,1275" fill="var(--teal)"/>
      <polygon points="0,1275 634,1012 634,1275" fill="var(--mint)"/>
    </svg>
    <h1 class="roles-title">PDP<br>Roles &amp;<br>Responsibilities:</h1>
    <table class="roles-table">
      <colgroup><col class="c-owner"><col class="c-svc"></colgroup>
      <thead><tr><th>Owner</th><th>Veridan Service</th></tr></thead>
      <tbody>
        <tr><td class="owner">Sets Project Objectives</td><td class="svc">Develops Delivery Plans</td></tr>
        <tr><td class="owner">Approves Major Decisions</td><td class="svc">Provides Recommendations</td></tr>
        <tr><td class="owner">Holds Project Risk</td><td class="svc">Identifies and Manages Risks</td></tr>
        <tr><td class="owner">Awards Contracts</td><td class="svc">Manages Contractor Interfaces</td></tr>
        <tr><td class="owner">Provides Funding</td><td class="svc">Monitors Cost and Schedule Performance</td></tr>
      </tbody>
    </table>
    <h2 class="heading abs" style="left:34px;top:636px">PDP Benefits:</h2>
    <ul class="ticks" style="top:689px">
      <li><svg viewBox="0 0 14 14"><path d="M2 7.5 L5.5 11 L12 3" fill="none" stroke="var(--teal)" stroke-width="2"/></svg>Provides owners with access to experienced project delivery capability</li>
      <li><svg viewBox="0 0 14 14"><path d="M2 7.5 L5.5 11 L12 3" fill="none" stroke="var(--teal)" stroke-width="2"/></svg>Improved project controls and governance</li>
      <li><svg viewBox="0 0 14 14"><path d="M2 7.5 L5.5 11 L12 3" fill="none" stroke="var(--teal)" stroke-width="2"/></svg>Greater flexibility than traditional EPC delivery</li>
      <li><svg viewBox="0 0 14 14"><path d="M2 7.5 L5.5 11 L12 3" fill="none" stroke="var(--teal)" stroke-width="2"/></svg>Enhanced visibility and management of cost, schedule and risk</li>
      <li><svg viewBox="0 0 14 14"><path d="M2 7.5 L5.5 11 L12 3" fill="none" stroke="var(--teal)" stroke-width="2"/></svg>Scalable resources aligned with project phases</li>
    </ul>
    <h2 class="heading abs" style="left:33px;top:868px">PDP Challenges:</h2>
    <ul class="ticks" style="top:920px">
      <li><svg viewBox="0 0 14 14"><path d="M2 7.5 L5.5 11 L12 3" fill="none" stroke="var(--teal)" stroke-width="2"/></svg>Owner retains significant delivery risk</li>
      <li><svg viewBox="0 0 14 14"><path d="M2 7.5 L5.5 11 L12 3" fill="none" stroke="var(--teal)" stroke-width="2"/></svg>Requires clear governance and decision-making processes</li>
      <li><svg viewBox="0 0 14 14"><path d="M2 7.5 L5.5 11 L12 3" fill="none" stroke="var(--teal)" stroke-width="2"/></svg>Multiple contractor interfaces require strong coordination</li>
      <li><svg viewBox="0 0 14 14"><path d="M2 7.5 L5.5 11 L12 3" fill="none" stroke="var(--teal)" stroke-width="2"/></svg>Success depends on collaborative Owner-PDP relationship</li>
    </ul>
  </section>

  <section class="panel panel--people">
    <h1 class="people-title">Key Veridan<br>Personnel</h1>
    <div class="rule" style="top:192px"></div>

    <article class="person" style="top:235px">
      <svg class="avatar" viewBox="0 0 110 110" aria-hidden="true"><circle cx="55" cy="55" r="53" fill="var(--teal-avatar)" stroke="#cfdcdc" stroke-width="3"/><circle cx="55" cy="42" r="13" fill="none" stroke="#fff" stroke-width="5"/><path d="M20 94 C26 72 84 72 90 94" fill="none" stroke="#fff" stroke-width="5"/></svg>
      <div class="person-body" style="top:-2px">
        <div class="person-head"><span>Karl Dunmore</span><span>35yrs Exp:</span><span>Executive Director</span></div>
        <p class="firms">Coralind Energy, Tarrow Petroleum, Kestrel, Ironbark Energy</p>
        <p>Extensive global energy industry experience, from frontline O&amp;M to the boardroom. Respected ‘C Suite’ leader with a track record of building high performing teams that deliver outstanding results.</p>
      </div>
    </article>
    <div class="rule" style="top:393px"></div>

    <article class="person" style="top:419px">
      <svg class="avatar" viewBox="0 0 110 110" aria-hidden="true"><circle cx="55" cy="55" r="53" fill="var(--teal-avatar)" stroke="#cfdcdc" stroke-width="3"/><circle cx="55" cy="42" r="13" fill="none" stroke="#fff" stroke-width="5"/><path d="M20 94 C26 72 84 72 90 94" fill="none" stroke="#fff" stroke-width="5"/></svg>
      <div class="person-body" style="left:133px;top:-2px">
        <div class="person-head"><span>Graham Shields</span><span>39yrs Exp:</span><span>Technical Director</span></div>
        <p class="firms">Coralind Energy, Tarrow Petroleum, Halvard Desert Oil,<br>Norva, Alder Group, Brolga, Kestrel, Ironbark Energy</p>
        <p>Highly skilled &amp; experienced operations &amp; project management professional with 39 years’ experience in the global oil &amp; gas industry delivering multiple projects and establishing best in class operational assets. Deep knowledge of project management, construction, commissioning &amp; start-up including a global functional assurance role.</p>
      </div>
    </article>
    <div class="rule" style="top:642px"></div>

    <article class="person" style="top:665px">
      <svg class="avatar" viewBox="0 0 110 110" aria-hidden="true"><circle cx="55" cy="55" r="53" fill="var(--teal-avatar)" stroke="#cfdcdc" stroke-width="3"/><circle cx="55" cy="42" r="13" fill="none" stroke="#fff" stroke-width="5"/><path d="M20 94 C26 72 84 72 90 94" fill="none" stroke="#fff" stroke-width="5"/></svg>
      <div class="person-body" style="left:133px;top:8px">
        <div class="person-head"><span>Ross Morley</span><span>40yrs Exp:</span><span>Commercial Director</span></div>
        <p class="firms">Calloway Energy, Pellora, Norva, Kestrel, Ironbark Energy</p>
        <p>Senior Logistics &amp; Supply Chain Manager / Procurement Manager with strong operational, commercial, project management, negotiating &amp; relationship building skills. Experienced in operating complex and diverse logistics operations, significantly improving service levels whilst reducing cost.</p>
      </div>
    </article>
    <div class="rule" style="top:879px"></div>

    <article class="person" style="top:901px">
      <svg class="avatar" viewBox="0 0 110 110" aria-hidden="true"><circle cx="55" cy="55" r="53" fill="var(--teal-avatar)" stroke="#cfdcdc" stroke-width="3"/><circle cx="55" cy="42" r="13" fill="none" stroke="#fff" stroke-width="5"/><path d="M20 94 C26 72 84 72 90 94" fill="none" stroke="#fff" stroke-width="5"/></svg>
      <div class="person-body" style="left:133px;top:8px;width:430px">
        <div class="person-head"><span>Joel Sinclair</span><span>27yrs Exp:</span><span>Operations Director</span></div>
        <p class="firms">Norva, Alder Group, Brolga, Kestrel, Ironbark Energy</p>
        <p>27 years’ success leading operations, maintenance and commissioning teams on onshore and offshore oil and gas production platforms, FPSOs, gas processing, coal seam gas, refrigeration facilities, and chemical refineries.<br>Results driven and enthusiastic Leader with a proven track record of delivery.</p>
      </div>
    </article>

    <div class="contact-box"><strong>For More Information Contact:</strong><br>directors@veridan.com.au</div>
  </section>

  <div class="band band--left"></div>
  <div class="band band--mid"></div>
  <div class="band band--right"></div>
</div>
</body>
</html>
```